The Harbourlight CV consultant

The service is premium. It is aimed at people 18-30, so students and those looking to change their first job, principally in the UK but also global. It is offering a very personalised CV writing service and is much more expensive than others on offer. I am very keen that it should look simple and premium. It needs to look very professional, reflecting the aspirational jobs that the clients will be applying for.
If there were three words that summed it up: modern, clean, premium.
I am waiting for all the testimonials to come in but they need to form a major part of the website.
I am also waiting for the full logo design files so that I can upload them. In the meantime there is a copy of the logo.
Thoughts to help those yet to send a design...
This is a premium service and some of the designs have looked very generic. The focus needs to be on quality and the process mentioned in the brief. The partnership and the advantages it brings are crucial but few have mentioned that.

```html
<!DOCTYPE html>
<html lang="en">
<head>
<meta charset="utf-8">
<title>The Harbourlight CV consultant – Website Design</title>
<link rel="stylesheet" href="https://fonts.googleapis.com/css2?family=Cinzel:wght@400&family=Inter:wght@400;500&display=swap">
<style>
:root{
  --slate:#626367;
  --blue:#0e74bc;
  --sky:#a3d6fa;
  --mist:#e0eef9;
  --frost:#f1f7fb;
  --board:#d5d7db;
  --ink:#3d3f44;
  --muted:#7b7d82;
  --white:#ffffff;
  --serif:'Cinzel', 'Times New Roman', serif;
  --sans:'Inter', Arial, sans-serif;
}
*{box-sizing:border-box;margin:0;padding:0}
html,body{width:1200px;height:2816px;overflow:hidden}
body{background:var(--board);font-family:var(--sans);color:var(--ink);position:relative}

/* Brand name: plain text in the body font, one colour, one weight */
.brand-name{font-family:var(--sans);font-weight:500;color:var(--blue);white-space:nowrap}

/* Brand board header */
.board-brand{position:absolute;left:184px;top:110px;font-size:16px}
.board-fonts{position:absolute;left:504px;top:100px}
.board-label{font-family:var(--sans);font-size:25px;color:#2c2d31;font-weight:400}
.board-fonts .f-serif{font-family:var(--serif);font-size:19px;color:var(--slate);margin-top:16px;letter-spacing:1px}
.board-fonts .f-sans{font-size:13px;color:var(--slate);margin-top:6px}
.board-colors{position:absolute;left:782px;top:100px}
.swatches{display:flex;gap:7px;margin-top:12px}
.swatch{width:42px;text-align:center}
.swatch i{display:block;width:42px;height:42px;border-radius:50%}
.swatch span{display:block;font-size:8.5px;color:#2c2d31;margin-top:6px}

/* Website */
.site{position:absolute;left:202px;top:273px;width:796px;height:2441px;background:var(--white);overflow:hidden}
.abs{position:absolute}
.nav-brand{left:13px;top:13px;font-size:10px}
.nav-links{left:334px;top:14px;display:flex;gap:30px;font-size:7.5px;color:var(--muted)}
.nav-cta{left:716px;top:6px;width:69px;height:25px;border:1px solid var(--blue);border-radius:3px;color:var(--blue);font-size:7.5px;display:flex;align-items:center;justify-content:center}

.photo{position:absolute}
.hero{left:11px;top:37px;width:774px;height:365px;background:linear-gradient(100deg,#2c3440 0%,#4a5563 40%,#7b8796 70%,#a9b4bf 100%)}
.hero-title{left:109px;top:204px;font-family:var(--serif);color:var(--white);font-size:37px;line-height:1.1;font-weight:400}
.hero-sub{left:109px;top:295px;color:var(--white);font-size:8.5px}
.btn{position:absolute;background:var(--blue);color:var(--white);font-size:7.5px;font-weight:500;border-radius:2px;display:flex;align-items:center;justify-content:center}

.section-title{position:absolute;font-family:var(--serif);font-size:26px;line-height:1.14;color:var(--slate);font-weight:400;white-space:nowrap}
.copy{position:absolute;font-size:8px;line-height:1.7;color:var(--muted)}
.copy.dark{color:var(--ink)}
.questions p{margin-bottom:4px}

.band{left:11px;top:820px;width:774px;height:403px;background:var(--frost)}
.card{position:absolute;top:958px;height:187px;background:var(--white);padding:28px 30px 0}
.quote{width:16px;height:12px}
.card p{font-size:7.8px;line-height:1.6;color:var(--muted);margin-top:10px}
.author{display:flex;align-items:center;gap:8px;margin-top:14px}
.avatar{width:22px;height:22px;border-radius:50%;background:linear-gradient(#c9cfd6,#8e98a4)}
.author b{display:block;font-weight:400;font-size:7.5px;color:var(--blue)}
.author small{display:block;font-size:6.5px;color:var(--muted)}

.checks{list-style:none}
.checks li{display:flex;align-items:center;gap:8px;font-size:8px;color:var(--ink);margin-bottom:8.5px}
.checks svg{width:11px;height:11px}

.cta{left:11px;top:1945px;width:774px;height:300px;background:linear-gradient(95deg,#26303c 0%,#3e4a58 35%,#8290a0 70%,#b7c2cd 100%)}
.cta-title{left:108px;top:1992px;font-family:var(--serif);color:var(--white);font-size:31px;line-height:1.02;font-weight:400}
.cta-copy{left:108px;top:2068px;width:280px;color:var(--white);font-size:8px;line-height:1.7}

.footer{left:11px;top:2245px;width:774px;height:185px;background:var(--mist)}
.footer-brand{left:109px;top:2300px;font-size:10px}
.footer-head{position:absolute;top:2297px;font-family:var(--serif);color:var(--blue);font-size:13px}
.socials{left:342px;top:2325px;display:flex;gap:4px}
.socials i{width:16px;height:16px;border:1px solid var(--slate);border-radius:50%;display:block}
.contact{left:540px;top:2325px;font-size:7.5px;color:var(--ink);line-height:1.9}
.contact span{display:inline-block;width:54px}
.legal{left:540px;top:2374px;font-size:6.5px;color:var(--muted)}
</style>
</head>
<body>

<div class="board-brand brand-name">The Harbourlight CV consultant</div>
<div class="board-fonts">
  <div class="board-label">Fonts:</div>
  <div class="f-serif">TRAJAN</div>
  <div class="f-sans">Neue Haas Unica Pro</div>
</div>
<div class="board-colors">
  <div class="board-label">Colors:</div>
  <div class="swatches">
    <div class="swatch"><i style="background:var(--slate)"></i><span>#626367</span></div>
    <div class="swatch"><i style="background:var(--blue)"></i><span>#0e74bc</span></div>
    <div class="swatch"><i style="background:var(--sky)"></i><span>#a3d6fa</span></div>
    <div class="swatch"><i style="background:var(--mist)"></i><span>#e0eef9</span></div>
    <div class="swatch"><i style="background:var(--frost)"></i><span>#f1f7fb</span></div>
  </div>
</div>

<main class="site">
  <!-- Navigation -->
  <div class="abs nav-brand brand-name">The Harbourlight CV consultant</div>
  <nav class="abs nav-links"><span>About</span><span>Services</span><span>Testimonials</span></nav>
  <div class="abs nav-cta">Get in Touch</div>

  <!-- Hero -->
  <div class="photo hero" role="img" aria-label="Smiling consultant in a suit handing a CV across a desk to a client in an office"></div>
  <h1 class="abs hero-title">Your Tailored<br>CV Consultant</h1>
  <p class="abs hero-sub">Invest in a CV writing partnership with Tom, the tailored CV consultant.</p>
  <div class="btn" style="left:109px;top:326px;width:73px;height:26px">Write Your CV</div>

  <!-- Partner section -->
  <h2 class="section-title" style="left:109px;top:446px">Your Partner in<br>Premium CV Writing</h2>
  <div class="photo" style="left:107px;top:525px;width:317px;height:202px;background:linear-gradient(#dbe9f6,#d6e6f5)" role="img" aria-label="Sample CV layouts fanned out on a pale blue background"></div>
  <p class="copy" style="left:455px;top:447px;width:232px">At Harbourlight, we elevate your professional narrative through premium writing services. Our tailored strategic solutions ensure your career story shines brightly, guiding you through every step of professional journey with expertise.</p>
  <div class="copy dark questions" style="left:455px;top:520px;width:250px">
    <p>Is your current CV not getting you results?</p>
    <p>Do you want to create a CV that stands out from the crowd?</p>
    <p>Do you want to get a job more quickly?</p>
    <p>Do you want to earn more for the job your searching for?</p>
  </div>
  <p class="copy" style="left:455px;top:599px;width:240px">If so then invest in a CV writing partnership with Tom Ellery, the tailored CV consultant.</p>
  <div class="photo" style="left:455px;top:650px;width:234px;height:119px;background:linear-gradient(110deg,#4a525c,#b9c0c8 55%,#2b3038)" role="img" aria-label="Hands reviewing a printed curriculum vitae with a pen"></div>

  <!-- Testimonials -->
  <div class="abs band"></div>
  <h2 class="section-title" style="left:109px;top:866px">But First, Take a<br>Look at Testimonials</h2>
  <p class="copy dark" style="left:455px;top:867px;width:240px">These are real results from real people. They invested in the partnership approach, and they're delighted because it works. The blurb that follows is not as important as what they say – I'd love it if you were the next person to appear</p>

  <article class="card" style="left:107px;width:270px">
    <svg class="quote" viewBox="0 0 16 12"><path fill="#626367" d="M0 6a6 6 0 0 1 6-6v3a3 3 0 0 0-2 2h3v7H0zM9 6a6 6 0 0 1 6-6v3a3 3 0 0 0-2 2h3v7H9z"/></svg>
    <p>Tom's approach to crafting my CV completely changed my job search. Within weeks of working together, I landed multiple interviews for positions I had previously been overlooked for. His personalized guidance not only enhanced my CV but also boosted my confidence!</p>
    <div class="author"><i class="avatar" role="img" aria-label="Client portrait"></i><div><b>Maya Hartley</b><small>- Student</small></div></div>
  </article>
  <article class="card" style="left:391px;width:269px">
    <svg class="quote" viewBox="0 0 16 12"><path fill="#626367" d="M0 6a6 6 0 0 1 6-6v3a3 3 0 0 0-2 2h3v7H0zM9 6a6 6 0 0 1 6-6v3a3 3 0 0 0-2 2h3v7H9z"/></svg>
    <p>Investing in Tom's CV writing partnership was one of the best decisions I've made for my career. His hands-on approach and insightful feedback helped me showcase my skills and experience in a way that truly resonated with employers.</p>
    <div class="author"><i class="avatar" role="img" aria-label="Client portrait"></i><div><b>Owen Pryce</b><small>- Student</small></div></div>
  </article>
  <article class="card" style="left:675px;width:270px">
    <svg class="quote" viewBox="0 0 16 12"><path fill="#626367" d="M0 6a6 6 0 0 1 6-6v3a3 3 0 0 0-2 2h3v7H0zM9 6a6 6 0 0 1 6-6v3a3 3 0 0 0-2 2h3v7H9z"/></svg>
    <p>Tom's approach to crafting my CV completely changed my job search. Within weeks of working together, I landed multiple interviews for positions I had previously been overlooked for. His personalized guidance not only enhanced my CV but also boosted my confidence!</p>
    <div class="author"><i class="avatar" role="img" aria-label="Client portrait"></i><div><b>Maya Hartley</b><small>- Student</small></div></div>
  </article>
  <svg class="abs" style="left:107px;top:1164px" width="40" height="10" viewBox="0 0 40 10"><path d="M15 5H2M6 1 2 5l4 4M25 5h13M34 1l4 4-4 4" fill="none" stroke="#626367" stroke-width="1"/></svg>

  <!-- Confidence section -->
  <h2 class="section-title" style="left:109px;top:1268px">WHERE CONFIDENCE MEETS CAPABILITY</h2>
  <div class="photo" style="left:107px;top:1317px;width:581px;height:328px;background:linear-gradient(100deg,#dcdfe2,#c8ccd1 45%,#e9ebed)" role="img" aria-label="Young professional woman in glasses reading documents at a bright office desk"></div>
  <div class="photo" style="left:78px;top:1666px;width:301px;height:220px;background:linear-gradient(160deg,#2e3a52,#c9ced5 55%,#e4e6ea)" role="img" aria-label="Interviewer and candidate reviewing a CV across a table"></div>
  <p class="copy" style="left:400px;top:1672px;width:290px">And you'll also get this. As a result of my approach everyone I've worked with is better prepared for interview. Our partnership will:</p>
  <ul class="abs checks" style="left:400px;top:1717px">
    <li><svg viewBox="0 0 11 11"><circle cx="5.5" cy="5.5" r="5.5" fill="#e0eef9"/><path d="M3 5.6l1.8 1.8L8 4" fill="none" stroke="#0e74bc" stroke-width="1"/></svg>Increase self awareness</li>
    <li><svg viewBox="0 0 11 11"><circle cx="5.5" cy="5.5" r="5.5" fill="#e0eef9"/><path d="M3 5.6l1.8 1.8L8 4" fill="none" stroke="#0e74bc" stroke-width="1"/></svg>Improve presentation skills</li>
    <li><svg viewBox="0 0 11 11"><circle cx="5.5" cy="5.5" r="5.5" fill="#e0eef9"/><path d="M3 5.6l1.8 1.8L8 4" fill="none" stroke="#0e74bc" stroke-width="1"/></svg>Build the right sort of confidence</li>
  </ul>
  <p class="copy" style="left:400px;top:1784px;width:290px">And as a result you'll impress at interview. You'll develop a language and way of expressing yourself that shows the very best of you. And as that language sinks in and becomes part of you, you project a genuine confidence, quietly powerful, that recruiters will want in their teams.</p>

  <!-- Partnership CTA -->
  <div class="photo cta" role="img" aria-label="Smiling consultant shaking hands with a client in a modern office"></div>
  <h2 class="abs cta-title">THE TAILORED CV<br>PARTNERSHIP</h2>
  <div class="abs cta-copy">
    <p>The key to all this success is our partnership. In our sessions, we will, together, build a CV. You will be working one to one, working with you for four sessions. There is a formula to this work but it is not formulaic. Your CV will be personal, you will shine.</p>
    <p style="margin-top:6px">So, take the first step to the future you can have.</p>
  </div>
  <div class="btn" style="left:108px;top:2168px;width:72px;height:26px">Contact Me</div>

  <!-- Footer -->
  <div class="abs footer"></div>
  <div class="abs footer-brand brand-name">The Harbourlight CV consultant</div>
  <div class="footer-head" style="left:342px">Follow Me</div>
  <div class="abs socials"><i></i><i></i><i></i></div>
  <div class="footer-head" style="left:540px">Get In Touch</div>
  <div class="abs contact">
    <div><span>Phone:</span>+44 100 200 300</div>
    <div><span>Email:</span>hello@harbourlightcv.co.uk</div>
  </div>
  <div class="abs legal">Harbourlight © 2024 - All Rights Reserved | Privacy Policy</div>
</main>

</body>
</html>
```